Business Card/Letterhead for Construction Company
Ronald Pike Construction
Professional
Ronald P. Pike
5702 Meadowlark Court, Suite #4
Fairhaven, OR 97999
ronald@ronaldpikeconstruction.example
www.ronaldpikeconstruction.example
Possibly add Facebook page:
www.friendpages.example/pikehouses
Navy Logo
Main Logo

```html
<!DOCTYPE html>
<html lang="en">
<head>
<meta charset="utf-8">
<title>Ronald Pike Construction – Business Card</title>
<link rel="stylesheet" href="https://fonts.googleapis.com/css2?family=Marcellus+SC&family=Marcellus&display=swap">
<style>
  :root {
    --navy: #1c3563;
    --navy-soft: #2b4a7e;
    --ink: #33405a;
    --paper: #ffffff;
    --backdrop: #eceef1;
    --faint: #dfe3e8;
  }
  * { box-sizing: border-box; margin: 0; padding: 0; }
  html, body {
    width: 1200px; height: 980px; overflow: hidden;
    background: var(--backdrop);
  }
  .canvas { position: relative; width: 1200px; height: 980px; }
  .card {
    position: absolute; left: 250px; width: 700px; height: 400px;
    background: var(--paper); border-radius: 22px; overflow: hidden;
    box-shadow: 0 6px 22px rgba(20, 30, 50, 0.12);
  }
  .card--front { top: 60px; }
  .card--back { top: 520px; }

  .brand {
    position: absolute; left: 40px; top: 42px;
    display: flex; align-items: center; gap: 14px;
  }
  .brand__mark { width: 40px; height: 40px; background: var(--navy); flex: none; }
  .brand__name {
    font-family: "Marcellus SC", serif; font-size: 27px;
    color: var(--navy); letter-spacing: 0.5px; white-space: nowrap;
  }

  .contact-list {
    position: absolute; left: 40px; top: 136px; list-style: none;
    font-family: "Marcellus", serif; font-size: 12.5px; color: var(--ink);
    line-height: 21px;
  }
  .contact-list li { display: flex; align-items: center; gap: 10px; white-space: nowrap; }
  .contact-list .dot {
    width: 9px; height: 9px; border-radius: 50%; background: var(--navy); flex: none;
  }
  .contact-list .indent { padding-left: 19px; }

  .swoosh { position: absolute; left: 0; top: 0; }

  .holder-name {
    position: absolute; right: 250px; top: 330px;
    font-family: "Marcellus SC", serif; font-size: 20px;
    color: var(--navy); letter-spacing: 0.5px; white-space: nowrap;
  }

  .back-url {
    position: absolute; left: 40px; top: 40px;
    font-family: "Marcellus SC", serif; font-size: 13px;
    color: var(--navy); letter-spacing: 1.2px;
  }
  .back-name {
    position: absolute; right: 50px; top: 170px;
    font-family: "Marcellus SC", serif; font-size: 44px;
    color: var(--faint); white-space: nowrap;
  }
</style>
</head>
<body>
<main class="canvas">
  <section class="card card--front" aria-label="Business card front">
    <svg class="swoosh" width="700" height="400" viewBox="0 0 700 400" aria-hidden="true">
      <path d="M648 70 C 620 210, 560 320, 452 400 L 468 400 C 574 322, 634 214, 660 70 Z" fill="var(--navy-soft)"/>
      <path d="M700 110 C 680 240, 630 330, 545 400 L 700 400 Z" fill="var(--navy)"/>
    </svg>

    <div class="brand">
      <span class="brand__mark"></span>
      <span class="brand__name">Ronald Pike Construction</span>
    </div>

    <ul class="contact-list">
      <li><span class="dot"></span>5702 Meadowlark Court, Suite #4</li>
      <li class="indent">Fairhaven, OR 97999</li>
      <li><span class="dot"></span>P 555.014.2280</li>
      <li><span class="dot"></span>F 555.014.2281</li>
      <li><span class="dot"></span>ronald@ronaldpikeconstruction.example</li>
      <li><span class="dot"></span>www.ronaldpikeconstruction.example</li>
    </ul>

    <p class="holder-name">Ronald P. Pike</p>
  </section>

  <section class="card card--back" aria-label="Business card back">
    <p class="back-url">www.ronaldpikeconstruction.example</p>
    <p class="back-name">Ronald Pike Construction</p>
  </section>
</main>
</body>
</html>
```